We need an eye catching logo design and Business Card that portrays our business, which is the cleaning and protecting of stainless steel with an organic non chemical product. This can be separate to the company name or can incorporate it. Maybe even just the company name itself. Company Name is Gleamwell Gleamwell.
Ideal for products exposed to weather elements, ie: balustrading, enclosures, BBQs, we also supply the product so you can do it yourself (DIY).
In addition we would want to include on this card:
1. My Name (Dean Horrocks)
2. Mobile No. (TBA Later)
3. Email address (TBA Later)
4. Web address (TBA Later)
Updates

Please note that we also need suggestions on a logo, as this we do not have this either.

Please note we have update our brief to be more specific.

Thank You.

Dean

Target Market(s)

Purchasing officers and government people.

Industry/Entity Type

Steel

Colors

Designer to choose colors to be used in the design.

Requirements
Must have
• 1. Name (Dean Horrocks)
2. Mobile No. (TBA Later)
Should not have
• Should not be to busy looking

```html
<!DOCTYPE html>
<html lang="en">
<head>
<meta charset="utf-8">
<title>Gleamwell Gleamwell — Business Card</title>
<link rel="stylesheet" href="https://fonts.googleapis.com/css2?family=Tinos:wght@400;700&display=swap">
<style>
  :root {
    --page: #ffffff;
    --steel-dark: #0d0f10;
    --steel-mid: #3a3f42;
    --steel-light: #c9d0d3;
    --steel-shine: #eef3f5;
    --accent-red: #e0271b;
    --name-gold: #f5a516;
    --text-white: #ffffff;
    --title-silver: #d4d9dc;
    --icon-blue: #0b8fd9;
    --icon-blue-light: #5cc6f7;
  }
  * { margin: 0; padding: 0; box-sizing: border-box; }
  html, body {
    width: 1200px; height: 702px; overflow: hidden;
    background: var(--page);
  }
  .stage { position: relative; width: 1200px; height: 702px; }
  .card {
    position: absolute; left: 59px; top: 55px;
    width: 1084px; height: 590px; overflow: hidden;
    font-family: "Tinos", "Times New Roman", serif;
  }
  .card-surface { position: absolute; inset: 0; width: 100%; height: 100%; }
  .company-title {
    position: absolute; left: 0; right: 0; top: 26px;
    text-align: center; font-weight: 700; font-size: 78px;
    color: var(--title-silver); letter-spacing: 0.5px; line-height: 1;
  }
  .brand-mark {
    position: absolute; left: 96px; top: 392px;
    font-weight: 700; font-size: 40px; color: var(--title-silver); line-height: 1;
  }
  .divider {
    position: absolute; left: 358px; top: 330px; width: 14px; height: 200px;
    border-left: 3px solid var(--steel-light); border-right: 3px solid var(--steel-light);
  }
  .person { position: absolute; left: 600px; width: 380px; text-align: center; }
  .person-name {
    position: absolute; top: 186px; right: 114px; white-space: nowrap;
    font-weight: 700; font-size: 50px; color: var(--name-gold); line-height: 1;
  }
  .person-role {
    position: absolute; top: 248px; left: 689px; width: 200px; text-align: center;
    font-weight: 700; font-size: 31px; color: var(--name-gold); line-height: 1;
  }
  .contact-line {
    position: absolute; right: 129px; white-space: nowrap;
    font-size: 31px; color: var(--text-white); line-height: 1.13; text-align: right;
  }
  .contact-address { top: 313px; }
  .contact-phone { top: 412px; }
  .contact-email { top: 496px; }
  .contact-icon { position: absolute; left: 980px; width: 52px; height: 52px; }
  .icon-address { top: 314px; }
  .icon-phone { top: 400px; }
  .icon-email { top: 485px; }
</style>
</head>
<body>
<div class="stage">
  <div class="card">
    <svg class="card-surface" viewBox="0 0 1084 590" preserveAspectRatio="none" aria-hidden="true">
      <defs>
        <linearGradient id="base-steel" x1="0" y1="0" x2="1" y2="1">
          <stop offset="0" stop-color="#4b5154"/>
          <stop offset="0.45" stop-color="#2a2e30"/>
          <stop offset="0.75" stop-color="#3c4144"/>
          <stop offset="1" stop-color="#050606"/>
        </linearGradient>
        <linearGradient id="upper-steel" x1="0" y1="0" x2="1" y2="0.4">
          <stop offset="0" stop-color="#3d4447"/>
          <stop offset="0.3" stop-color="#6c7579"/>
          <stop offset="0.6" stop-color="#eef3f5"/>
          <stop offset="0.8" stop-color="#7d878b"/>
          <stop offset="1" stop-color="#3f4548"/>
        </linearGradient>
        <radialGradient id="icon-fill" cx="0.4" cy="0.3" r="0.8">
          <stop offset="0" stop-color="var(--icon-blue-light)"/>
          <stop offset="1" stop-color="var(--icon-blue)"/>
        </radialGradient>
      </defs>
      <rect width="1084" height="590" fill="url(#base-steel)"/>
      <path d="M0 0 H1084 V122 C800 110 500 150 0 300 Z" fill="url(#upper-steel)"/>
      <path d="M0 300 C500 150 800 110 1084 122 V155 C700 150 450 190 0 330 Z" fill="var(--steel-dark)"/>
      <path d="M0 328 C450 188 700 150 1084 155" fill="none" stroke="var(--accent-red)" stroke-width="5"/>
    </svg>

    <h1 class="company-title">Gleamwell Gleamwell</h1>
    <div class="brand-mark">Gleamwell</div>
    <div class="divider"></div>

    <div class="person-name">Dean Horrocks</div>
    <div class="person-role">Director</div>

    <p class="contact-line contact-address">4180&nbsp; Larchmont Ave.<br>604417 Riverton</p>
    <p class="contact-line contact-phone">555-014-2386</p>
    <p class="contact-line contact-email">gleamwellgleamwell@mailbox.net</p>

    <svg class="contact-icon icon-address" viewBox="0 0 52 52" aria-hidden="true">
      <circle cx="26" cy="26" r="25" fill="url(#icon-fill)" stroke="#dff3fd" stroke-width="1.5"/>
      <path d="M12 26 L26 13 L40 26 Z" fill="#fff"/>
      <rect x="16" y="25" width="20" height="14" fill="#fff"/>
      <rect x="23" y="30" width="6" height="9" fill="var(--icon-blue)"/>
    </svg>
    <svg class="contact-icon icon-phone" viewBox="0 0 52 52" aria-hidden="true">
      <circle cx="26" cy="26" r="25" fill="url(#icon-fill)" stroke="#dff3fd" stroke-width="1.5"/>
      <path d="M34 14 l4 4 c1 1 1 2 0 3 l-3 3 c-3 5 -6 8 -11 11 l-3 3 c-1 1 -2 1 -3 0 l-4 -4 l5 -5 l3 3 c3 -2 6 -5 8 -8 l-3 -3 Z" fill="#fff"/>
    </svg>
    <svg class="contact-icon icon-email" viewBox="0 0 52 52" aria-hidden="true">
      <circle cx="26" cy="26" r="25" fill="url(#icon-fill)" stroke="#dff3fd" stroke-width="1.5"/>
      <rect x="13" y="17" width="26" height="18" fill="#fff"/>
      <path d="M13 17 L26 28 L39 17" fill="none" stroke="var(--icon-blue)" stroke-width="1.8"/>
    </svg>
  </div>
</div>
</body>
</html>
```